NEW STORE PROMOTION FLYER

We need a flyer design for a new lingerie store based in Double Bay.
The people living in Double Bay are most wealthy suburb in Sydney. Our customers are aged at 30+ to 70.
We are offering 'up to 30% off' on selected products.
we recommend using our theme colour: light pink, red, white
the address is:
shop 5/214 Marlow Crest Rd, NSW 2173
contact number: 02 8415 3907
We need key information:
1. we want to let neighborhood know that we open a new store.
2. we offer 'up to 30% off' Christmas Sale
3. Please use our theme colour: light pink, red, white
4. Please add the address map on flyer (you may design again if you need )
5.open hour:
Mon - Fri 10:00am - 5:30pm
Sat - Sun 10:00am - 5:30pm
thank you
aged 30+ to 70; they are relatively wealthy.
Store

```html
<!DOCTYPE html>
<html lang="en">
<head>
<meta charset="utf-8">
<title>Velvetta Lingerie – New Store</title>
<link rel="stylesheet" href="https://fonts.googleapis.com/css2?family=EB+Garamond:ital,wght@0,400;0,600;1,400;1,600&display=swap">
<style>
  :root {
    --pink: #e23a80;
    --pink-soft: #f3abc8;
    --pink-pale: #f6c6d8;
    --red: #cf2530;
    --white: #ffffff;
    --rule: #e2e2e2;
    --photo-light: #f4f2f1;
    --photo-mid: #cfc5bf;
    --photo-dark: #7a6a60;
    --map-pink: #f5c0d4;
    --map-road: #ffffff;
    --map-ink: #5a4a52;
  }
  * { box-sizing: border-box; margin: 0; padding: 0; }
  html, body { width: 848px; height: 1200px; overflow: hidden; background: var(--white); }
  body { font-family: "EB Garamond", Georgia, serif; }

  .flyer { position: relative; width: 848px; height: 1200px; overflow: hidden; background: var(--white); }

  .hero-photo {
    position: absolute; left: 300px; top: 0; width: 548px; height: 1129px;
    background:
      radial-gradient(ellipse 55% 45% at 62% 62%, var(--photo-dark) 0%, rgba(122,106,96,0.55) 45%, rgba(122,106,96,0) 75%),
      radial-gradient(ellipse 30% 22% at 50% 30%, #8a6a58 0%, rgba(138,106,88,0) 80%),
      linear-gradient(180deg, var(--photo-light) 0%, var(--photo-mid) 70%, #b9aea8 100%);
  }
  .hero-fade {
    position: absolute; left: 300px; top: 0; width: 260px; height: 1129px;
    background: linear-gradient(90deg, var(--white) 0%, rgba(255,255,255,0) 100%);
  }

  .brand {
    position: absolute; left: 54px; top: 74px; width: 760px;
    color: var(--pink); font-weight: 600; font-size: 116px; line-height: 1;
    letter-spacing: -1px; white-space: nowrap;
  }

  .new-tag {
    position: absolute; left: 0; top: 292px; width: 228px; height: 57px;
    background: var(--pink); border-radius: 0 12px 12px 0;
    color: var(--white); font-style: italic; font-size: 60px; line-height: 57px;
    padding-left: 52px;
  }
  .store-word {
    position: absolute; left: 54px; top: 349px;
    color: var(--pink); font-size: 76px; line-height: 1; letter-spacing: 1px;
  }
  .tagline { position: absolute; left: 54px; top: 418px; width: 246px; text-align: center; }
  .tagline span { display: block; line-height: 1; }
  .tag-comfortable { color: var(--pink); font-weight: 600; font-size: 44px; }
  .tag-supportive { color: var(--pink-pale); font-size: 38px; margin: -16px 0 0 34px; }
  .tag-sexy { color: var(--red); font-style: italic; font-size: 62px; margin-top: -18px; }

  .hours {
    position: absolute; left: 0; top: 581px; width: 350px; height: 92px;
    border-top: 2px solid var(--rule); border-bottom: 2px solid var(--rule);
    padding: 12px 0 0 54px;
  }
  .hours-row { display: flex; font-size: 23px; line-height: 34px; }
  .hours-day { color: var(--pink); font-style: italic; font-weight: 600; width: 114px; }
  .hours-time { color: var(--pink-soft); }

  .address {
    position: absolute; left: 60px; top: 692px;
    color: var(--pink-soft); font-style: italic; font-size: 33px; line-height: 36px;
  }

  .sale {
    position: absolute; left: 60px; top: 810px;
    color: var(--red); font-style: italic; font-size: 24px; line-height: 30px; white-space: nowrap;
  }
  .sale strong { font-weight: 600; }

  .store-map {
    position: absolute; left: 52px; top: 862px; width: 246px; height: 246px;
    border-radius: 50%; overflow: hidden; background: var(--map-pink);
  }
  .store-map svg { display: block; }
  .map-label { font-family: "EB Garamond", Georgia, serif; fill: var(--map-ink); }

  .slogan {
    position: absolute; left: 352px; top: 1012px;
    color: var(--white); font-style: italic; font-size: 100px; line-height: 1; white-space: nowrap;
  }

  .footer-band {
    position: absolute; left: 0; top: 1129px; width: 848px; height: 71px;
    background: var(--pink);
  }
  .footer-call {
    position: absolute; right: 64px; top: 18px;
    color: var(--white); font-size: 26px; line-height: 32px;
  }
  .footer-call em { font-size: 30px; }
</style>
</head>
<body>
<main class="flyer">
  <div class="hero-photo" role="img" aria-label="Photograph of a woman in a taupe lace camisole seated on white bedding"></div>
  <div class="hero-fade"></div>

  <h1 class="brand">Velvetta Lingerie</h1>

  <div class="new-tag">NEW</div>
  <div class="store-word">STORE</div>
  <p class="tagline">
    <span class="tag-comfortable">comfortable</span>
    <span class="tag-supportive">supportive</span>
    <span class="tag-sexy">sexy</span>
  </p>

  <section class="hours">
    <div class="hours-row"><span class="hours-day">Mon - Fri</span><span class="hours-time">10:00am - 5:30pm</span></div>
    <div class="hours-row"><span class="hours-day">Sat - Sun</span><span class="hours-time">10:00am - 5:30pm</span></div>
  </section>

  <address class="address">Shop 5/214<br>Marlow Crest Rd,<br>NSW, 2173</address>

  <p class="sale">Christmas Sale – <strong>up to 30% off</strong></p>

  <div class="store-map" role="img" aria-label="Street map showing the store location on Marlow Crest Rd">
    <svg width="246" height="246" viewBox="0 0 246 246">
      <g class="map-pin" transform="translate(112 58)">
        <path d="M16 0C7 0 0 7 0 16c0 12 16 30 16 30s16-18 16-30C32 7 25 0 16 0z" fill="var(--pink)"/>
        <circle cx="16" cy="16" r="6" fill="var(--white)"/>
      </g>
      <text class="map-label" x="123" y="138" text-anchor="middle" font-size="16" font-style="italic">Marlow Crest Rd</text>
      <text class="map-label" x="123" y="186" text-anchor="middle" font-size="12">Shop 5/214 Marlow Crest Rd, NSW</text>
    </svg>
  </div>

  <p class="slogan">Just for you</p>

  <footer class="footer-band">
    <p class="footer-call">Call us on <em>02 8415 3907</em></p>
  </footer>
</main>
</body>
</html>
```